" Somos uma fábrica de Creme de Café, um produto inovador tanto no sabor quanto no modo de preparo. O Café Velurê é um creme de café 100% arábica, saborizado naturalmente que faz uma bebida extremamente cremosa e diferenciada. Até quem não gosta de café, quando prova o Café Velurê passa a gostar. Nossos produtos são 100% naturais e nosso café é de altíssima qualidade, pois utilizamos café 100% arábica. Buscamos constante inovação na formulação de nossos produtos. Temos uma linguagem de comunicação informal, leve e descontraída com nossos clientes, sem ser infantil, . "

```html
<!DOCTYPE html>
<html lang="pt-BR">
<head>
<meta charset="UTF-8">
<title>Café Velurê — rótulos creme de café</title>
<link href="https://fonts.googleapis.com/css2?family=Lilita+One&family=Kaushan+Script&family=Nunito:wght@600;800&display=swap" rel="stylesheet">
<style>
  :root {
    --bg: #ebe7e4;
    --cream: #f4eee7;
    --red: #e2474d;
    --red-dark: #c23a40;
    --brown: #5b3b32;
    --brown-dark: #472d26;
    --ink: #3a2a25;
    --line: rgba(0,0,0,0.12);
  }
  * { box-sizing: border-box; margin: 0; padding: 0; }
  html, body { width: 1200px; height: 1200px; overflow: hidden; background: var(--bg); }
  body { font-family: "Nunito", sans-serif; color: var(--ink); position: relative; }

  .label {
    --brand: var(--red);
    --brand-dark: var(--red-dark);
    position: absolute; left: 50px; width: 1100px; height: 520px;
    display: grid; grid-template-columns: 260px 580px 260px;
    background: var(--cream);
    box-shadow: 0 10px 30px rgba(0,0,0,0.08);
  }
  .label--red { top: 50px; }
  .label--brown { top: 630px; --brand: var(--brown); --brand-dark: var(--brown-dark); }

  .panel { position: relative; display: flex; flex-direction: column; }
  .panel__top { height: 56%; padding: 30px 20px 0; }
  .panel__bottom { flex: 1; background: var(--brand); }
  .panel--left .panel__top { border-right: 1px solid var(--line); padding-right: 92px; }
  .panel--right .panel__top { border-left: 1px solid var(--line); }

  .nutrition { border: 2px solid var(--ink); font-size: 11px; font-weight: 600; }
  .nutrition__title { font-weight: 800; font-size: 12px; padding: 4px 6px; border-bottom: 2px solid var(--ink); }
  .nutrition__row { display: flex; justify-content: space-between; gap: 6px; padding: 3px 6px; border-bottom: 1px solid var(--ink); white-space: nowrap; }
  .nutrition__row:last-child { border-bottom: none; }

  .claims { display: flex; flex-direction: column; gap: 14px; }
  .claims--left { position: absolute; right: 16px; top: 36px; width: 70px; }
  .claim { display: flex; flex-direction: column; align-items: center; gap: 3px; text-align: center;
    font-family: "Lilita One", sans-serif; font-size: 11px; color: var(--brand); text-transform: uppercase; line-height: 1.05; }
  .claim svg { width: 34px; height: 34px; }

  .prep { display: grid; grid-template-columns: 78px 1fr; gap: 10px; }
  .prep__title { font-family: "Kaushan Script", cursive; font-size: 21px; line-height: 1.2; color: var(--brand); margin-bottom: 6px; }
  .prep__text { font-size: 12.5px; font-weight: 600; line-height: 1.35; }
  .prep__tip { font-family: "Lilita One", sans-serif; font-size: 11px; color: var(--brand); text-transform: uppercase; margin-top: 8px; }

  .front { position: relative; display: flex; flex-direction: column; }
  .front__top { height: 56%; display: flex; flex-direction: column; align-items: center; justify-content: center; gap: 22px; }
  .front__claim { font-family: "Lilita One", sans-serif; font-size: 34px; color: var(--brand); }
  .brand { display: flex; align-items: center; gap: 16px; }
  .brand__dot { width: 22px; height: 22px; border-radius: 50%; background: var(--brand); }
  .brand__name { font-family: "Nunito", sans-serif; font-weight: 800; font-size: 64px; line-height: 1; color: var(--brand); }
  .front__bottom { flex: 1; background: var(--brand); color: var(--cream); display: flex; flex-direction: column; align-items: center; justify-content: center; position: relative; }
  .flavor-intro { font-family: "Lilita One", sans-serif; font-size: 26px; }
  .flavor-name { font-family: "Kaushan Script", cursive; font-size: 62px; line-height: 1.15; }
  .net-weight { position: absolute; right: 24px; bottom: 18px; font-family: "Lilita One", sans-serif; font-size: 24px; }
</style>
</head>
<body>

<section class="label label--red">
  <div class="panel panel--left">
    <div class="panel__top">
      <div class="nutrition">
        <div class="nutrition__title">Info. Nutricional</div>
        <div class="nutrition__row"><span>Porção 20g</span></div>
        <div class="nutrition__row"><span>Energia</span><span>80kcal</span></div>
        <div class="nutrition__row"><span>Carboidratos</span><span>15g</span></div>
        <div class="nutrition__row"><span>Proteínas</span><span>1g</span></div>
        <div class="nutrition__row"><span>Gorduras</span><span>2g</span></div>
        <div class="nutrition__row"><span>Sódio</span><span>5mg</span></div>
      </div>
      <div class="claims claims--left">
        <div class="claim"><svg viewBox="0 0 36 36"><circle cx="18" cy="18" r="15" fill="none" stroke="currentColor" stroke-width="3"/><line x1="8" y1="28" x2="28" y2="8" stroke="currentColor" stroke-width="3"/></svg>sem<br>lactose</div>
        <div class="claim"><svg viewBox="0 0 36 36"><circle cx="18" cy="18" r="15" fill="none" stroke="currentColor" stroke-width="3"/><line x1="8" y1="28" x2="28" y2="8" stroke="currentColor" stroke-width="3"/></svg>sem<br>glúten</div>
      </div>
    </div>
    <div class="panel__bottom"></div>
  </div>

  <div class="front">
    <div class="front__top">
      <div class="front__claim">100% arábica</div>
      <div class="brand"><span class="brand__dot"></span><span class="brand__name">Café Velurê</span></div>
    </div>
    <div class="front__bottom">
      <div class="flavor-intro">sabor natural de</div>
      <div class="flavor-name">Frutas Vermelhas</div>
      <div class="net-weight">180g</div>
    </div>
  </div>

  <div class="panel panel--right">
    <div class="panel__top">
      <div class="prep">
        <div class="claims">
          <div class="claim"><svg viewBox="0 0 36 36"><circle cx="18" cy="18" r="15" fill="none" stroke="currentColor" stroke-width="3"/><line x1="8" y1="28" x2="28" y2="8" stroke="currentColor" stroke-width="3"/></svg>sem<br>açúcar</div>
          <div class="claim"><svg viewBox="0 0 36 36"><circle cx="18" cy="18" r="15" fill="none" stroke="currentColor" stroke-width="3"/><line x1="8" y1="28" x2="28" y2="8" stroke="currentColor" stroke-width="3"/></svg>sem<br>conservante</div>
        </div>
        <div>
          <div class="prep__title">Modo de preparo</div>
          <p class="prep__text">Misture duas colheres com leite gelado e bata até ficar cremoso.</p>
          <div class="prep__tip">dica de preparo</div>
        </div>
      </div>
    </div>
    <div class="panel__bottom"></div>
  </div>
</section>

<section class="label label--brown">
  <div class="panel panel--left">
    <div class="panel__top">
      <div class="nutrition">
        <div class="nutrition__title">Info. Nutricional</div>
        <div class="nutrition__row"><span>Porção 20g</span></div>
        <div class="nutrition__row"><span>Energia</span><span>80kcal</span></div>
        <div class="nutrition__row"><span>Carboidratos</span><span>15g</span></div>
        <div class="nutrition__row"><span>Proteínas</span><span>1g</span></div>
        <div class="nutrition__row"><span>Gorduras</span><span>2g</span></div>
        <div class="nutrition__row"><span>Sódio</span><span>5mg</span></div>
      </div>
      <div class="claims claims--left">
        <div class="claim"><svg viewBox="0 0 36 36"><circle cx="18" cy="18" r="15" fill="none" stroke="currentColor" stroke-width="3"/><line x1="8" y1="28" x2="28" y2="8" stroke="currentColor" stroke-width="3"/></svg>sem<br>lactose</div>
        <div class="claim"><svg viewBox="0 0 36 36"><circle cx="18" cy="18" r="15" fill="none" stroke="currentColor" stroke-width="3"/><line x1="8" y1="28" x2="28" y2="8" stroke="currentColor" stroke-width="3"/></svg>sem<br>glúten</div>
      </div>
    </div>
    <div class="panel__bottom"></div>
  </div>

  <div class="front">
    <div class="front__top">
      <div class="front__claim">100% arábica</div>
      <div class="brand"><span class="brand__dot"></span><span class="brand__name">Café Velurê</span></div>
    </div>
    <div class="front__bottom">
      <div class="flavor-intro">sabor natural de</div>
      <div class="flavor-name">Avelãs</div>
      <div class="net-weight">180g</div>
    </div>
  </div>

  <div class="panel panel--right">
    <div class="panel__top">
      <div class="prep">
        <div class="claims">
          <div class="claim"><svg viewBox="0 0 36 36"><circle cx="18" cy="18" r="15" fill="none" stroke="currentColor" stroke-width="3"/><line x1="8" y1="28" x2="28" y2="8" stroke="currentColor" stroke-width="3"/></svg>sem<br>açúcar</div>
          <div class="claim"><svg viewBox="0 0 36 36"><circle cx="18" cy="18" r="15" fill="none" stroke="currentColor" stroke-width="3"/><line x1="8" y1="28" x2="28" y2="8" stroke="currentColor" stroke-width="3"/></svg>sem<br>conservante</div>
        </div>
        <div>
          <div class="prep__title">Modo de preparo</div>
          <p class="prep__text">Misture duas colheres com leite gelado e bata até ficar cremoso.</p>
          <div class="prep__tip">dica de preparo</div>
        </div>
      </div>
    </div>
    <div class="panel__bottom"></div>
  </div>
</section>

</body>
</html>
```